Flyer Design Project

Need a DL Size flyer (2 sided) for letter box marketing for our website www.brightwardsecure.com.au

Project Deadline Extended
Reason: Thank you for submitting the designs. We like few of the designs and will request those designers to changes few things to make it more suitable for us. Because of holidays need to extend the deadlines. Thank you.

Industry/Entity Type

Marketing

```html
<!DOCTYPE html>
<html lang="en">
<head>
<meta charset="utf-8">
<title>Brightward Secure – Camera Packages</title>
<link rel="stylesheet" href="https://fonts.googleapis.com/css2?family=Arimo:wght@700&family=Roboto+Condensed:wght@700&display=swap">
<style>
  :root {
    --sky-deep: #0c3a86;
    --sky-mid: #2766b8;
    --sky-light: #5e97d6;
    --band-navy: #1a2a66;
    --accent-yellow: #f6b81c;
    --text-white: #ffffff;
    --product-bg-top: #f4f5f7;
    --product-bg-bottom: #d9dde3;
  }
  * { margin: 0; padding: 0; box-sizing: border-box; }
  html, body { width: 1200px; height: 566px; overflow: hidden; background: var(--sky-deep); }
  .flyer {
    position: relative;
    width: 1200px;
    height: 566px;
    overflow: hidden;
    background:
      radial-gradient(ellipse 60% 80% at 50% 20%, rgba(120,170,230,0.45), transparent 70%),
      linear-gradient(180deg, var(--sky-mid) 0%, var(--sky-light) 45%, var(--sky-mid) 75%, var(--sky-deep) 100%);
  }
  .skyline {
    position: absolute;
    inset: 0 0 76px 0;
    background: linear-gradient(90deg, rgba(10,50,120,0.35), rgba(120,170,230,0.15) 50%, rgba(10,50,120,0.35));
  }
  .package {
    position: absolute;
    top: 0;
    width: 300px;
    text-align: center;
  }
  .package--one { left: 75px; }
  .package--two { left: 450px; }
  .package--three { left: 825px; }
  .package__title {
    font-family: "Arimo", Arial, sans-serif;
    font-weight: 700;
    font-size: 33px;
    color: var(--accent-yellow);
    margin-top: 44px;
    line-height: 40px;
    height: 40px;
  }
  .package__photo {
    display: block;
    width: 290px;
    height: 164px;
    margin: 8px auto 0;
    border-radius: 6px;
    background: linear-gradient(180deg, var(--product-bg-top), var(--product-bg-bottom));
  }
  .package__features {
    list-style: none;
    margin-top: 12px;
    font-family: "Roboto Condensed", "Arial Narrow", sans-serif;
    font-weight: 700;
    font-size: 16px;
    line-height: 23.2px;
    color: var(--text-white);
  }
  .promo-band {
    position: absolute;
    left: 0;
    right: 0;
    bottom: 0;
    height: 76px;
    background: var(--band-navy);
    display: flex;
    align-items: center;
    justify-content: center;
    font-family: "Arimo", Arial, sans-serif;
    font-weight: 700;
    font-size: 31px;
    color: var(--text-white);
  }
  .promo-band__url { color: var(--accent-yellow); margin-left: 9px; }
</style>
</head>
<body>
<main class="flyer">
  <div class="skyline" role="img" aria-label="Blue-tinted city office towers seen from below"></div>

  <section class="package package--one">
    <h2 class="package__title">Package 1</h2>
    <div class="package__photo" role="img" aria-label="Two white dome cameras, a DVR recorder and an LCD monitor"></div>
    <ul class="package__features">
      <li>2 X high resolution dome cameras</li>
      <li>1 X 4 channel standalone DVR</li>
      <li>500GB hard drive</li>
      <li>19″ LCD monitor</li>
      <li>Remote access from PCs &amp; Phones*</li>
      <li>Easy to use</li>
      <li>1 Year Warranty</li>
      <li>Full system supplied &amp; installed</li>
    </ul>
  </section>

  <section class="package package--two">
    <h2 class="package__title">Package 2</h2>
    <div class="package__photo" role="img" aria-label="Four white dome cameras, a DVR recorder and an LCD monitor"></div>
    <ul class="package__features">
      <li>4 X high resolution dome cameras</li>
      <li>1 X 4 channel standalone DVR</li>
      <li>500GB hard drive</li>
      <li>19″ LCD monitor</li>
      <li>Remote access from PCs &amp; Phones*</li>
      <li>Easy to use</li>
      <li>1 Year Warranty</li>
      <li>Full system supplied &amp; installed</li>
    </ul>
  </section>

  <section class="package package--three">
    <h2 class="package__title">Package 3</h2>
    <div class="package__photo" role="img" aria-label="Eight white dome cameras, a DVR recorder and an LCD monitor"></div>
    <ul class="package__features">
      <li>8 X high resolution dome cameras</li>
      <li>1 X 8 channel standalone DVR</li>
      <li>1 Terrabyte hard drive</li>
      <li>19″ LCD monitor</li>
      <li>Remote access from PCs &amp; Phones*</li>
      <li>Easy to use</li>
      <li>1 Year Warranty</li>
      <li>Full system supplied &amp; installed</li>
    </ul>
  </section>

  <footer class="promo-band">
    More packages online at<span class="promo-band__url">www.brightwardsecure.com.au</span>
  </footer>
</main>
</body>
</html>
```